Pediatric Dental Practice needs a postcard for direct mail advertising

We are looking for a creative and professional double-sided postcard design for a direct mail marketing campaign. Our goal is to attract new families to our pediatric dental practice by conveying a sense of warmth, modern care, and clinical excellence. The design should feel "boutique" and high-end yet remain fun and approachable for parents and children.

```html
<!DOCTYPE html>
<html lang="en">
<head>
<meta charset="utf-8">
<title>Maple Grove Pediatric Dentistry – Postcard</title>
<link rel="stylesheet" href="https://fonts.googleapis.com/css2?family=Lora:wght@500;600&family=Nunito+Sans:wght@400;600&family=Caveat:wght@500&display=swap">
<style>
:root{
  --backdrop:#064a52;
  --cream:#f7f4ee;
  --green:#5b8f55;
  --green-deep:#4f8249;
  --green-soft:#dfe8d6;
  --green-pale:#e8eee1;
  --ink:#3a3d42;
  --rule:#b9bdb6;
  --serif:'Lora', Georgia, serif;
  --sans:'Nunito Sans', Arial, sans-serif;
  --script:'Caveat', cursive;
}
*{margin:0;padding:0;box-sizing:border-box}
html,body{width:873px;height:1200px;overflow:hidden;background:var(--backdrop)}
.canvas{position:relative;width:873px;height:1200px}
.card{position:absolute;left:77px;width:720px;height:506px;background:var(--cream);overflow:hidden;box-shadow:0 6px 18px rgba(0,0,0,.3)}
.card--front{top:58px}
.card--back{top:626px}
.abs{position:absolute}

/* front */
.brand{left:30px;top:66px;width:150px;text-align:center}
.brand__mark{display:block;width:34px;height:34px;border-radius:50%;background:var(--green);margin:0 auto 8px}
.brand__name{font-family:var(--sans);font-weight:600;font-size:21px;color:var(--ink);line-height:1;letter-spacing:.3px}
.brand__sub{font-family:var(--sans);font-weight:600;font-size:7.5px;color:var(--ink);letter-spacing:2.2px;margin-top:4px}
.headline{left:40px;top:156px;font-family:var(--serif);font-weight:500;font-size:62px;line-height:60px;letter-spacing:-.5px}
.headline .g{color:var(--green)}
.headline .d{color:var(--ink)}
.divider{height:12px}
.divider::before,.divider::after{content:"";position:absolute;top:6px;height:1px;background:var(--rule);width:calc(50% - 14px)}
.divider::before{left:0}.divider::after{right:0}
.divider svg{position:absolute;left:50%;top:0;transform:translateX(-50%)}
.tagline{left:45px;top:376px;font-family:var(--sans);font-weight:600;font-size:11.5px;line-height:18px;letter-spacing:1px;color:var(--green)}
.pill{left:38px;top:427px;width:190px;height:44px;border-radius:22px;background:var(--green);box-shadow:0 0 0 3px #dfe6d6;color:#fff;display:flex;align-items:center;gap:12px;padding-left:18px;font-family:var(--sans);font-weight:600;font-size:12px;letter-spacing:1.2px;line-height:15px}
.photo{left:0;top:0}
.badge{left:538px;top:335px;width:160px;height:160px;border-radius:50%;background:var(--green);border:3px solid var(--cream);box-shadow:0 0 0 0 transparent;display:flex;flex-direction:column;align-items:center;justify-content:center;color:#fff;font-family:var(--serif);font-size:15.5px;line-height:20px;text-align:center}
.badge::after{content:"";position:absolute;inset:6px;border:1px dashed rgba(255,255,255,.7);border-radius:50%}
.badge svg{margin-bottom:6px}

/* back */
.intro{left:61px;top:34px;font-family:var(--serif);font-weight:500;font-size:26px;line-height:29px;color:var(--ink)}
.intro .g{color:var(--green)}
.intro-rule{left:61px;top:133px;width:167px}
.intro-copy{left:61px;top:163px;width:180px;font-family:var(--sans);font-size:11.4px;line-height:21px;color:var(--ink)}
.address-line{left:283px;height:1px;background:#8e918c}
.stamp{left:644px;top:16px;width:78px;height:82px;border:1px solid #333}
.services{left:284px;top:202px;width:436px;height:92px}
.services__sep{position:absolute;top:0;width:1px;height:92px;background:var(--rule)}
.service{position:absolute;display:flex;align-items:center;gap:8px;font-family:var(--sans);font-size:10.3px;line-height:13.5px;color:var(--ink)}
.service__icon{width:41px;height:41px;border-radius:50%;border:1.3px solid var(--green);display:flex;align-items:center;justify-content:center;flex:none}
.coupon{left:63px;top:325px;width:252px;height:139px;background:var(--green);border-radius:10px;color:#fff;text-align:center;box-shadow:0 3px 6px rgba(0,0,0,.12)}
.coupon::before{content:"";position:absolute;inset:5px;border:1.3px dashed rgba(255,255,255,.75);border-radius:8px}
.coupon__notch{position:absolute;left:50%;top:-14px;transform:translateX(-50%);width:34px;height:34px;border-radius:50%;background:var(--cream);display:flex;align-items:center;justify-content:center}
.coupon__amount{position:absolute;left:0;right:0;top:14px;font-family:var(--serif);font-weight:500;font-size:56px;line-height:60px}
.coupon__amount small{font-size:37px;letter-spacing:1px}
.coupon__line{position:absolute;left:0;right:0;font-family:var(--sans);letter-spacing:.6px}
.contact{left:334px;top:327px;width:400px;height:163px;background:var(--green-pale);border-radius:12px}
.contact__sep{position:absolute;left:191px;top:20px;width:1px;height:124px;background:#b9c2b0}
.contact__item{position:absolute;left:24px;display:flex;gap:11px;align-items:flex-start;font-family:var(--sans);font-size:11px;line-height:15px;color:var(--ink)}
.contact__item svg{flex:none;margin-top:1px}
.cta{position:absolute;left:215px;top:22px;color:var(--green)}
.cta__small{font-family:var(--serif);font-size:16px;letter-spacing:2px;line-height:18px}
.cta__big{font-family:var(--serif);font-weight:500;font-size:25px;line-height:28px;letter-spacing:.5px}
.cta__script{font-family:var(--script);font-size:20px;line-height:24px;color:var(--ink);margin-top:8px}
.cta__heart{margin:2px 0 0 95px}
</style>
</head>
<body>
<div class="canvas">

  <!-- FRONT -->
  <section class="card card--front">
    <svg class="abs photo" width="720" height="506" viewBox="0 0 720 506">
      <defs>
        <linearGradient id="roomTone" x1="0" y1="0" x2="1" y2="1">
          <stop offset="0" stop-color="#e6e2c9"/>
          <stop offset=".45" stop-color="#d9d1a6"/>
          <stop offset=".7" stop-color="#c9b98a"/>
          <stop offset="1" stop-color="#5fa89a"/>
        </linearGradient>
      </defs>
      <g role="img" aria-label="Photo of a bright pediatric treatment room with a teal dental chair, two small chairs and a window">
        <path d="M335 0 H720 V506 H335 C318 470 300 420 320 380 C345 330 300 300 312 240 C322 185 305 130 330 70 C338 45 330 20 335 0 Z" fill="url(#roomTone)"/>
      </g>
      <path d="M380 506 C470 480 520 460 600 450 C660 443 700 455 720 460 V506 Z" fill="#cfdcc4"/>
    </svg>

    <div class="abs brand">
      <span class="brand__mark"></span>
      <div class="brand__name">maple grove</div>
      <div class="brand__sub">PEDIATRIC DENTISTRY</div>
    </div>

    <h1 class="abs headline"><span class="g">Healthy<br>smiles</span><br><span class="d">grow here.</span></h1>

    <div class="abs divider" style="left:45px;top:354px;width:244px">
      <svg width="14" height="12" viewBox="0 0 24 22"><path d="M12 21 C4 14 0 10 0 6 A6 6 0 0 1 12 4 A6 6 0 0 1 24 6 C24 10 20 14 12 21Z" fill="var(--green)"/></svg>
    </div>

    <p class="abs tagline">GENTLE CARE. MODERN TECHNOLOGY.<br>MADE FOR KIDS.</p>

    <div class="abs pill">
      <svg width="21" height="19" viewBox="0 0 24 22"><path d="M12 21 C4 14 0 10 0 6 A6 6 0 0 1 12 4 A6 6 0 0 1 24 6 C24 10 20 14 12 21Z" fill="#fff"/></svg>
      <span>NOW WELCOMING<br>NEW FAMILIES</span>
    </div>

    <div class="abs badge">
      <svg width="16" height="14" viewBox="0 0 24 22"><path d="M12 21 C4 14 0 10 0 6 A6 6 0 0 1 12 4 A6 6 0 0 1 24 6 C24 10 20 14 12 21Z" fill="#fff"/></svg>
      <span>Where little<br>smiles feel<br>right at home.</span>
    </div>
  </section>

  <!-- BACK -->
  <section class="card card--back">
    <h2 class="abs intro">A better dental<br><span class="g">experience</span> for<br>your child.</h2>
    <div class="abs divider intro-rule">
      <svg width="13" height="11" viewBox="0 0 24 22"><path d="M12 21 C4 14 0 10 0 6 A6 6 0 0 1 12 4 A6 6 0 0 1 24 6 C24 10 20 14 12 21Z" fill="var(--green)"/></svg>
    </div>
    <p class="abs intro-copy">At Maple Grove Pediatric Dentistry, we combine clinical excellence with compassion to help your child feel confident, comfortable, and cared for—every step of the way.</p>

    <div class="abs address-line" style="top:68px;width:320px"></div>
    <div class="abs address-line" style="top:96px;width:320px"></div>
    <div class="abs address-line" style="top:124px;width:457px"></div>
    <div class="abs address-line" style="top:153px;width:457px"></div>
    <div class="abs address-line" style="top:181px;width:457px"></div>
    <div class="abs stamp"></div>

    <div class="abs services">
      <span class="services__sep" style="left:0"></span>
      <span class="services__sep" style="left:143px"></span>
      <span class="services__sep" style="left:294px"></span>

      <div class="service" style="left:29px;top:-3px">
        <span class="service__icon"><svg width="20" height="22" viewBox="0 0 20 22" fill="none" stroke="var(--green)" stroke-width="1.3"><path d="M4 2 C1 2 0 6 1.5 10 C3 14 3 20 5 20 C7 20 7 14 10 14 C13 14 13 20 15 20 C17 20 17 14 18.5 10 C20 6 19 2 16 2 C13 2 12 4 10 4 C8 4 7 2 4 2Z"/></svg></span>
        <span>Preventive<br>Care</span></div>
      <div class="service" style="left:29px;top:51px">
        <span class="service__icon"><svg width="20" height="20" viewBox="0 0 20 20" fill="none" stroke="var(--green)" stroke-width="1.3"><circle cx="10" cy="11" r="7"/><path d="M10 4 V2"/><circle cx="10" cy="11" r="1.5"/></svg></span>
        <span>Emergency<br>Visits</span></div>
      <div class="service" style="left:168px;top:-3px">
        <span class="service__icon"><svg width="20" height="22" viewBox="0 0 20 22" fill="none" stroke="var(--green)" stroke-width="1.3"><path d="M4 2 C1 2 0 6 1.5 10 C3 14 3 20 5 20 C7 20 7 14 10 14 C13 14 13 20 15 20 C17 20 17 14 18.5 10 C20 6 19 2 16 2 C13 2 12 4 10 4 C8 4 7 2 4 2Z"/></svg></span>
        <span>Restorative<br>Dentistry</span></div>
      <div class="service" style="left:168px;top:51px">
        <span class="service__icon"><svg width="26" height="14" viewBox="0 0 26 14" fill="none" stroke="var(--green)" stroke-width="1.3"><rect x="1" y="2" width="7" height="10" rx="3"/><rect x="9.5" y="2" width="7" height="10" rx="3"/><rect x="18" y="2" width="7" height="10" rx="3"/><path d="M0 7 H26"/></svg></span>
        <span>Orthodontic<br>Evaluations</span></div>
      <div class="service" style="left:319px;top:-3px">
        <span class="service__icon"><svg width="22" height="22" viewBox="0 0 22 22" fill="none" stroke="var(--green)" stroke-width="1.3"><circle cx="11" cy="11" r="9"/></svg></span>
        <span>Sedation<br>Options</span></div>
      <div class="service" style="left:319px;top:51px">
        <span class="service__icon"><svg width="24" height="16" viewBox="0 0 24 16" fill="none" stroke="var(--green)" stroke-width="1.3"><path d="M12 1 C15 5 15 10 12 15 C9 10 9 5 12 1Z"/><path d="M12 15 C7 15 3 12 2 7 C6 7 10 10 12 15Z"/><path d="M12 15 C17 15 21 12 22 7 C18 7 14 10 12 15Z"/></svg></span>
        <span>Calm, Comfortable<br>Environment</span></div>
    </div>

    <div class="abs coupon">
      <span class="coupon__notch"><svg width="17" height="15" viewBox="0 0 24 22"><path d="M12 21 C4 14 0 10 0 6 A6 6 0 0 1 12 4 A6 6 0 0 1 24 6 C24 10 20 14 12 21Z" fill="var(--green)"/></svg></span>
      <div class="coupon__amount">$50 <small>OFF</small></div>
      <div class="coupon__line" style="top:82px;font-size:13.5px;font-weight:600">YOUR CHILD’S FIRST VISIT!</div>
      <div class="coupon__line" style="top:109px;font-size:11.5px">MENTION THIS CARD.</div>
    </div>

    <div class="abs contact">
      <div class="contact__item" style="top:24px">
        <svg width="11" height="14" viewBox="0 0 12 16"><path d="M6 0 A6 6 0 0 1 12 6 C12 10 6 16 6 16 C6 16 0 10 0 6 A6 6 0 0 1 6 0Z" fill="var(--green)"/><circle cx="6" cy="6" r="2.2" fill="var(--green-pale)"/></svg>
        <span>456 Orchard Lane, Suite 200<br>Brookfield, SC 29000</span></div>
      <div class="contact__item" style="top:66px">
        <svg width="12" height="12" viewBox="0 0 24 24"><path d="M6.6 10.8 C8 13.6 10.4 16 13.2 17.4 L15.4 15.2 C15.7 14.9 16.1 14.8 16.4 15 C17.5 15.4 18.8 15.6 20 15.6 C20.6 15.6 21 16 21 16.6 V20 C21 20.6 20.6 21 20 21 C10.6 21 3 13.4 3 4 C3 3.4 3.4 3 4 3 H7.5 C8.1 3 8.5 3.4 8.5 4 C8.5 5.3 8.7 6.5 9.1 7.6 C9.2 7.9 9.1 8.3 8.9 8.6Z" fill="var(--green)"/></svg>
        <span>(555) 010-2345</span></div>
      <div class="contact__item" style="top:94px">
        <svg width="12" height="12" viewBox="0 0 24 24" fill="none" stroke="var(--green)" stroke-width="2.4"><circle cx="12" cy="12" r="10"/><path d="M2 12 H22 M12 2 C8 6 8 18 12 22 C16 18 16 6 12 2"/></svg>
        <span>maplegrovekids.com</span></div>
      <div class="contact__item" style="top:121px">
        <svg width="12" height="12" viewBox="0 0 12 12"><rect width="12" height="12" rx="2" fill="var(--green)"/></svg>
        <span>@maplegrovekids</span></div>
      <span class="contact__sep"></span>
      <div class="cta">
        <div class="cta__small">SCHEDULE</div>
        <div class="cta__big">TODAY!</div>
        <div class="cta__script">We can’t wait to<br>meet your little one!</div>
        <svg class="cta__heart" width="11" height="10" viewBox="0 0 24 22"><path d="M12 21 C4 14 0 10 0 6 A6 6 0 0 1 12 4 A6 6 0 0 1 24 6 C24 10 20 14 12 21Z" fill="var(--green)"/></svg>
      </div>
    </div>
  </section>

</div>
</body>
</html>
```